Webdesign für Naturheilpraktiker gesucht
Zielgruppe
Ich arbeite im Gesundheitswesen als Naturheilpraktiker Traditionell Tibetische Medizin.
Verfüge aber über verschiedene Anwendungstechniken.
Die Zielgruppe sind alle Menschen die mehr als nur klassische Medizin wollen, die mit der klassischen Schulmedizin nicht mehr weiter kommen und einen alternativen Weg suchen. Menschen die neben der Schulmedizin noch einen anderen Weg suchen.
Menschen im Wellness und Fitnessbereich.
Ernährungsbewusste Menschen.
Sportler allgemein da ich über eine neue Technik verfüge (KERVO) die erst auf den Markt kommt und mit der verschiedene Beschwerden gelindert werden können.
Grob gesagt alles was mit Medizin, Komplementärmedizin, Gesundheit, Wellness, Sport usw zu tun hat.
Kompetenzen der Traditionell Tibetische Medizin:
- Massage als Gesundheitssystem oder als Wellness
- Ernährungsberatung
- tibetisches Yoga
- Lebensberatung
- Familienstellen
Aufgabenstellung
Der Firmennamen und das Logo bestehen.
In der Tradition der tibetischen Medizin ist vor allem Blau (Medizin Buddha) die Farben sind aber frei wählbar.
Es soll Vertrautheit, Geborgenheit und Wärme ausstrahlen.
Nicht zu feminin erscheinen.
Einfach ein paar Ideen
http://massagepraxis-wolfrin.example
http://www.himalheilkunde.example

```html
<!DOCTYPE html>
<html lang="de">
<head>
<meta charset="utf-8">
<title>Lotusweg – Tibetische Massage</title>
<link href="https://fonts.googleapis.com/css2?family=Open+Sans:wght@300;400;600&family=Baloo+2:wght@700&family=Roboto:wght@500;700&display=swap" rel="stylesheet">
<style>
:root{
  --blue:#1e94d6;
  --green:#7ac14d;
  --text:#555;
  --heading:#444;
  --line:#ddd;
  --white:#fff;
}
*{box-sizing:border-box;margin:0;padding:0}
html,body{width:859px;height:1200px;overflow:hidden;background:var(--white)}
body{position:relative;font-family:"Open Sans",sans-serif;font-weight:300;color:var(--text)}
.abs{position:absolute}
.topline{left:0;top:0;width:859px;height:2px;background:var(--green)}
.brand{left:217px;top:14px;width:90px;height:70px;text-align:center}
.brand-dot{width:40px;height:40px;border-radius:50%;background:var(--blue);margin:6px auto 8px}
.brand-name{font-family:"Open Sans",sans-serif;font-weight:600;font-size:8px;letter-spacing:2px;color:var(--blue)}
.nav{left:344px;top:18px;display:flex;font-size:7.6px;font-weight:400;color:var(--heading)}
.nav a{display:block;height:19px;line-height:19px;padding:0 5px;margin-right:6px;color:inherit;text-decoration:none}
.nav a.active{background:var(--blue);color:var(--white);padding:0 7px}
.hero{left:0;top:95px;width:859px;height:176px;background:var(--blue)}
.hero-title{left:193px;top:118px;font-family:"Baloo 2",sans-serif;font-weight:700;font-size:22px;color:var(--white);letter-spacing:-.3px}
.hero-text{left:193px;top:155px;font-size:7px;line-height:16.4px;color:var(--white);font-weight:300}
.card{top:228px;width:236px;height:81px;background:var(--white)}
.media{position:absolute}
.card-title{font-size:14.5px;line-height:14.5px;font-weight:300;color:var(--heading)}
.card-desc{font-size:7px;line-height:11px;margin-top:9px}
.card-link{font-size:7.5px;color:var(--green);font-weight:400;margin-top:6px;display:block}
.tile{top:347px;width:118px;height:118px;background:var(--green);color:var(--white);padding:12px 11px}
.tile .card-title{color:var(--white)}
.tile .card-link{color:var(--white)}
.content{left:203px;top:490px;width:455px;font-size:7px;line-height:10.7px}
.content h2{font-size:15px;font-weight:300;color:var(--heading);line-height:18px;margin-bottom:4px}
.content p{margin-bottom:5.7px}
.content ul{margin:0 0 5px 13px}
.article{left:203px;width:320px}
.article h3{font-size:13.8px;line-height:14.5px;font-weight:400;color:var(--green);letter-spacing:-.25px;white-space:nowrap}
.thumb{width:90px;height:60px;border:2px solid #f0f0f0}
.excerpt{font-size:7px;line-height:10.7px}
.btn{display:block;border:1px solid var(--green);border-radius:2px;color:var(--green);font-family:"Roboto",sans-serif;font-weight:700;font-size:7px;text-align:center}
.divider{left:203px;width:308px;height:1px;background:var(--line)}
.footer{left:0;top:1170px;width:859px;height:30px;background:var(--blue);color:var(--white);font-size:6.5px;font-weight:400}
</style>
</head>
<body>
<div class="abs topline"></div>

<div class="abs brand">
  <div class="brand-dot"></div>
  <div class="brand-name">LOTUSWEG</div>
</div>

<nav class="abs nav">
  <a class="active">Home</a><a>Geschichte</a><a>Information</a><a>Kontakt</a>
</nav>

<section class="abs hero"></section>
<h1 class="abs hero-title">Tibetische Massage</h1>
<div class="abs hero-text">
  Die tibetische Massage hat seine Wurzeln schon in der Lehre Buddhas Shakyamuni.<br>
  Der Mensch wird als Ganzheit von Körper, Geist und Seele erfasst und Behandelt.<br>
  Nicht nur dem Körper sondern auch der Psyche oder dem Geist kommt besondere Bedeutung&nbsp; bei der Behandlung zu.<br>
  Die Massage eignet sich vor allem für psychosomatische Beschwerden.
</div>

<article class="abs card" style="left:193px">
  <div class="media" role="img" aria-label="Foto: Ölmassage am Rücken" style="left:0;top:0;width:119px;height:81px;background:linear-gradient(135deg,#d9b9a0,#f1ebe6 60%,#8a5a44)"></div>
  <div class="abs" style="left:129px;top:12px;width:100px">
    <div class="card-title">Gesund im<br>Kindesalter</div>
    <div class="card-desc">Lernen Sie mehr zur Gesundheit Ihrer Kinder</div>
    <span class="card-link">mehr lesen</span>
  </div>
</article>
<article class="abs card" style="left:430px">
  <div class="media" role="img" aria-label="Foto: Blüten, Kerzen und Klangschale" style="left:0;top:0;width:118px;height:79px;background:radial-gradient(circle at 50% 45%,#d4502a,#3c3d42 55%)"></div>
  <div class="abs" style="left:129px;top:12px;width:104px">
    <div class="card-title">Kräuter<br>Medizin</div>
    <div class="card-desc">Hier finden Sie Informationen aus der Welt der Kräuter</div>
    <span class="card-link">mehr lesen</span>
  </div>
</article>

<article class="abs tile" style="left:193px">
  <div class="card-title">Ingwer<br>Tee</div>
  <div class="card-desc">Rezepte und Wissenswertes zu Ingwer Tee</div>
  <span class="card-link">mehr lesen</span>
</article>
<div class="abs" role="img" aria-label="Foto: Klangschalenbehandlung" style="left:312px;top:347px;width:118px;height:118px;background:linear-gradient(160deg,#2f7d6c,#c8453a 45%,#5a3a2c)"></div>
<article class="abs tile" style="left:430px">
  <div class="card-title">Vorteile von<br>Tee</div>
  <div class="card-desc">Warum Tee so gut ist für Ihre Gesundheit</div>
  <span class="card-link">mehr lesen</span>
</article>
<div class="abs" role="img" aria-label="Illustration: Meditierende Silhouette mit Chakren" style="left:548px;top:347px;width:118px;height:118px;background:linear-gradient(180deg,#a4532f,#5a2a1a 55%,#120806)"></div>

<section class="abs content">
  <h2>Die Grundlagen der Tibetischen Medizin</h2>
  <p>Die Grundlagen der Tibetischen Medizin bilden die drei Körperenergien</p>
  <p>Lung (Wind) – Tripa (Feuer) – Badkan (Schleim)</p>
  <p>die für die Körperfunktion und auch den Geisteszustand verantwortlich sind.</p>
  <p>Sind alle drei Energien im Gleichgewicht erfreuen wir uns bester Gesundheit.</p>
  <p>In der Tibetischen Massage ist es das Ziel die drei Energien auszugleichen und somit das Gleichgewicht herzustellen. Die tibetische Massage ist eine ganzheitliche, tief wirkende Massage die die innere Stabilität und den Heilprozess fördert.</p>
  <p>Sie eignet sich daher sehr gut zur Unterstützung anderer Therapien und oder zur Entspannung.</p>
  <p>Es ist eine je nach Symptomen sanfte oder kräftige Ölmassage die unter anderem Verspannungen und Energieblockaden löst und das physische und psychische Wohlbefinden fördert.</p>
  <p>Besonders hilfreich bei:</p>
  <ul>
    <li>- Verspannungen</li><li>- Schlafstörungen</li><li>- Nervosität</li><li>- Unruhe</li>
    <li>- Stress</li><li>- Verwirrtheit</li><li>- Konzentrationsschwäche</li><li>- Energielosigkeit</li>
  </ul>
  <p>und zur Entspannung im Allgemeinen (Wellness)</p>
</section>

<article class="abs article" style="top:808px">
  <h3>Homöopathie-Heilverfahren: Ideal für Kinder</h3>
  <div class="abs thumb" role="img" aria-label="Foto: Kind mit Globuli" style="left:0;top:15px;background:linear-gradient(135deg,#e9d8cc,#f7f4f2)"></div>
  <p class="abs excerpt" style="left:100px;top:15px;width:208px">Homöopathische Mittel eignen sich ganz besonders für die Behandlung von Kindern. Da sie bei ordnungsgemäßer Anwendung keine Nebenwirkungen verursachen, wirken homöopathische Mittel deutlich sanfter als Arzneien der Schulmedizin.</p>
  <span class="abs btn" style="left:100px;top:74px;width:63px;height:18px;line-height:16px">mehr</span>
</article>
<div class="abs divider" style="top:906px"></div>

<article class="abs article" style="top:916px">
  <h3>Wann Homöopathie-Verfahren nicht zur<br>Anwendung kommen</h3>
  <div class="abs thumb" role="img" aria-label="Foto: Fläschchen mit homöopathischen Mitteln" style="left:0;top:30px;background:linear-gradient(135deg,#8d8a7c,#d4d0c4)"></div>
  <p class="abs excerpt" style="left:100px;top:30px;width:208px">Eine homöopathische Behandlung kommt allerdings bei einigen Erkrankungen nicht oder nur ergänzend in Betracht.</p>
  <span class="abs btn" style="left:100px;top:56px;width:63px;height:18px;line-height:16px">mehr</span>
</article>
<div class="abs divider" style="top:1016px"></div>

<article class="abs article" style="top:1026px">
  <h3>Was Ihnen Ihr Arzt über die Homöopathie-<br>Therapie meistens nicht erzählt</h3>
  <div class="abs thumb" role="img" aria-label="Foto: Ärztin hält die Hand einer Patientin" style="left:0;top:30px;background:linear-gradient(135deg,#e8e8ea,#d9b7a3)"></div>
  <p class="abs excerpt" style="left:100px;top:30px;width:208px">Trotz überzeugender Website Erfahrungsberichte von Patienten, die sich homöopathisch behandeln ließen, raten Schulmediziner meist von einer alternativen Behandlung mit homöopathischen Mitteln ab.</p>
  <span class="abs btn" style="left:100px;top:78px;width:63px;height:18px;line-height:16px">mehr</span>
</article>
<span class="abs btn" style="left:203px;top:1129px;width:308px;height:21px;line-height:19px">Mehr Informationen</span>

<aside>
  <div class="abs" role="img" aria-label="Foto: Arzt im blauen Kittel" style="left:530px;top:807px;width:128px;height:110px;border:2px solid #f0f0f0;background:linear-gradient(180deg,#4a84b8,#5d95c4)"></div>
  <div class="abs" style="left:530px;top:925px;font-size:9px;font-weight:300;color:var(--heading)">Dr. Jonas Berger</div>
  <div class="abs" style="left:530px;top:951px;font-size:7px">Kontaktieren Sie uns für einen Termin</div>
  <span class="abs btn" style="left:530px;top:967px;width:126px;height:22px;line-height:20px">Kontakt</span>
</aside>

<footer class="abs footer">
  <span class="abs" style="left:193px;top:11px">© 2017 Homeopathy | Impressum | Datenschutz | Haftungsausschluss</span>
  <span class="abs" style="left:622px;top:9px;font-size:8px;width:44px;text-align:right">pagebau</span>
</footer>
</body>
</html>
```